Business Card Design For A Cajun Seafood Restaurant

We are opening a cajun seafood restaurant in a week. We mainly serve cajun seafood which is orginally from Louisiana. We want design on both sides of a business card. I have menu on the website. You can go to www.bayourelish.com to check out our menu.

Restaurant name: Marsh Kettle
Phone: +1 (555) 014-4172
Address: 48627 Dellmont Row, #5, Brackwater, LA 70999
Email: bayourelish@mailbox.example
Website: www.bayourelish.com

Maybe add social media icons (facebook, instagram) if looks nice on the business card.
facebook.com/bayourelish
instagram.com/bayourelish or @bayourelish

Attached is the logo and other business card samples that I like.

```html
<!DOCTYPE html>
<html lang="en">
<head>
<meta charset="utf-8">
<title>Marsh Kettle – Business Card</title>
<link rel="stylesheet" href="https://fonts.googleapis.com/css2?family=Open+Sans:wght@400;600;800&display=swap">
<style>
  :root{
    --stage:#e9e9e9;
    --ink:#111111;
    --paper:#ffffff;
    --orange:#f47a1f;
    --orange-deep:#e8620f;
    --yellow:#ffc400;
    --mascot-a:#f08a2c;
    --mascot-b:#c9531a;
    --light:#ffffff;
  }
  *{box-sizing:border-box;margin:0;padding:0}
  html,body{width:1200px;height:950px;overflow:hidden}
  body{background:var(--stage);font-family:"Open Sans",Arial,sans-serif;position:relative}
  .card{position:absolute;left:220px;width:760px;height:430px;overflow:hidden;box-shadow:0 6px 18px rgba(0,0,0,.18)}
  .card--front{top:30px;background:var(--ink)}
  .card--back{top:490px;background:var(--paper)}

  .brand{position:absolute;display:flex;flex-direction:column;align-items:center;width:300px}
  .card--front .brand{left:50%;top:80px;transform:translateX(-50%)}
  .card--back .brand{left:40px;top:120px}
  .brand__mascot{width:150px;height:120px;border-radius:46% 46% 40% 40%;background:radial-gradient(circle at 50% 40%,var(--mascot-a),var(--mascot-b))}
  .brand__name{margin-top:14px;font-weight:800;font-size:32px;letter-spacing:.5px;white-space:nowrap}
  .card--front .brand__name{color:var(--yellow)}
  .card--back .brand__name{color:var(--orange-deep)}

  .social{position:absolute;left:50%;top:320px;transform:translateX(-50%);display:flex;gap:22px;color:var(--light);font-size:16px;white-space:nowrap}
  .social__item{display:flex;align-items:center;gap:8px}
  .social__mark{width:13px;height:13px;background:var(--light);border-radius:2px}
  .social__mark--round{border-radius:50%}

  .panel{position:absolute;inset:0}
  .contact{position:absolute;right:40px;top:70px;text-align:right;color:var(--light)}
  .contact__name{font-size:24px;font-weight:600}
  .contact__title{font-size:16px;margin-bottom:18px}
  .contact__row{display:flex;align-items:center;justify-content:flex-end;gap:10px;font-size:16px;line-height:1.35;margin-top:6px;white-space:nowrap}
  .contact__row svg{flex:none;width:16px;height:16px}
</style>
</head>
<body>
  <section class="card card--front" aria-label="Card front">
    <div class="brand">
      <div class="brand__mascot" role="img" aria-label="Restaurant mascot illustration"></div>
      <div class="brand__name">Marsh Kettle</div>
    </div>
    <div class="social">
      <span class="social__item"><span class="social__mark"></span>bayourelish</span>
      <span class="social__item"><span class="social__mark social__mark--round"></span>@bayourelish</span>
    </div>
  </section>

  <section class="card card--back" aria-label="Card back">
    <svg class="panel" viewBox="0 0 760 430" aria-hidden="true">
      <polygon fill="var(--yellow)" points="448,0 760,0 760,430 398,430"/>
      <polygon fill="var(--orange)" points="460,0 760,0 760,430 410,430"/>
    </svg>
    <div class="brand">
      <div class="brand__mascot" role="img" aria-label="Restaurant mascot illustration"></div>
      <div class="brand__name">Marsh Kettle</div>
    </div>
    <div class="contact">
      <div class="contact__name">Marcus Fell</div>
      <div class="contact__title">President</div>
      <div class="contact__row"><span>48627 Dellmont Row, #5,<br>Brackwater, LA 70999</span>
        <svg viewBox="0 0 16 16"><path fill="var(--light)" d="M8 1a5 5 0 0 0-5 5c0 4 5 9 5 9s5-5 5-9a5 5 0 0 0-5-5zm0 7a2 2 0 1 1 0-4 2 2 0 0 1 0 4z"/></svg></div>
      <div class="contact__row"><span>+1 (555) 014-4172</span>
        <svg viewBox="0 0 16 16"><path fill="var(--light)" d="M4 1l2.5 3-1.5 2c1 2 3 4 5 5l2-1.5 3 2.5-2 2.5C7 14 2 9 1.5 3.5z"/></svg></div>
      <div class="contact__row"><span>bayourelish@mailbox.example</span>
        <svg viewBox="0 0 16 16"><rect x="1" y="3" width="14" height="10" rx="1" fill="var(--light)"/><path d="M1.5 3.5 8 9l6.5-5.5" fill="none" stroke="var(--orange)" stroke-width="1.3"/></svg></div>
      <div class="contact__row"><span>www.bayourelish.com</span>
        <svg viewBox="0 0 16 16"><circle cx="8" cy="8" r="6.5" fill="none" stroke="var(--light)" stroke-width="1.5"/><path d="M1.5 8h13M8 1.5c-3 3.5-3 9.5 0 13M8 1.5c3 3.5 3 9.5 0 13" fill="none" stroke="var(--light)" stroke-width="1.2"/></svg></div>
    </div>
  </section>
</body>
</html>
```